Have Logo - Need Business Card Design!!!

I am looking for a business card design for a real estate development business. The company name is Corvane Realty Partners. I already have a logo created by Sketch Harbor and would like this logo to be incorporated into the design. I have uploaded the files. The card needs to be professional, but visually interesting. Not necessary to be double-sided, but if you want to get creative and can think of something to put on the back then have at it.

Target Market(s)

The target audience for these business cards will be professionals in the real estate industry.

Industry/Entity Type

Real Estate

Requirements
Must have
• The business card must have all the necessary items for a business card, i.e. company name, our logo, name (however, not title necessary), office address, office phone number, cell number, fax number, website address, etc.

You can use the information below for the card:

Gregory L. Hanlon
782 Marlowe Avenue
San Francisco, California 94127

www.corvanerealty.example
ghanlon@corvanerealty.example
Office: 415-555-0142
Fax: 415-555-0143
Cell: 415-555-0186

```html
<!DOCTYPE html>
<html lang="en">
<head>
<meta charset="utf-8">
<title>Corvane Realty Partners — Business Card</title>
<link href="https://fonts.googleapis.com/css2?family=Cormorant+Garamond:wght@500&family=Open+Sans:wght@300;400&display=swap" rel="stylesheet">
<style>
  :root {
    --navy: #111551;
    --green: #006b2d;
    --paper: #fafafa;
    --ink: #4a4a4a;
    --backdrop: #d4d4d4;
    --white: #ffffff;
  }
  * { margin: 0; padding: 0; box-sizing: border-box; }
  html, body {
    width: 1200px; height: 900px; overflow: hidden;
    background: var(--backdrop);
  }
  .stage { position: relative; width: 1200px; height: 900px; }
  .card {
    position: absolute; left: 298px; width: 598px; height: 342px; overflow: hidden;
  }
  .card--front { top: 112px; background: var(--navy); }
  .card--back { top: 486px; background: var(--paper); }

  .brand {
    display: flex; align-items: center; gap: 10px;
    font-family: "Cormorant Garamond", serif; font-weight: 500;
    font-size: 34px; line-height: 1; white-space: nowrap;
  }
  .brand__square { display: block; flex: none; }
  .card--front .brand {
    position: absolute; left: 0; right: 0; top: 147px;
    justify-content: center; color: var(--white);
  }
  .card--front .brand__square { width: 56px; height: 56px; background: var(--green); }
  .card--back .brand {
    position: absolute; left: 29px; top: 26px;
    color: var(--green);
  }
  .card--back .brand__square { width: 52px; height: 52px; background: var(--navy); }

  .website {
    position: absolute; left: 0; right: 0; top: 296px; text-align: center;
    font-family: "Open Sans", sans-serif; font-weight: 300; font-size: 19px;
    color: var(--white);
  }

  .address, .contacts {
    position: absolute; left: 29px;
    font-family: "Open Sans", sans-serif; font-weight: 300; font-size: 15.5px;
    color: var(--ink);
  }
  .address { top: 160px; font-style: normal; line-height: 20px; }
  .contacts { top: 237px; list-style: none; line-height: 21.5px; }
  .contacts li { display: flex; align-items: center; gap: 8px; }
  .contacts svg { width: 14px; height: 12px; flex: none; fill: var(--green); }

  .person {
    position: absolute; right: 24px; top: 226px; text-align: right;
  }
  .person__name {
    font-family: "Cormorant Garamond", serif; font-weight: 500;
    font-size: 27px; color: var(--green); line-height: 30px;
  }
  .person__title {
    font-family: "Open Sans", sans-serif; font-weight: 300;
    font-size: 15.5px; color: var(--ink); line-height: 20px;
  }
  .accent {
    position: absolute; right: 24px; bottom: 0; display: flex; gap: 4px;
  }
  .accent span { width: 28px; height: 39px; display: block; }
  .accent .accent--navy { background: var(--navy); }
  .accent .accent--green { background: var(--green); }
</style>
</head>
<body>
<main class="stage">
  <section class="card card--front" aria-label="Card front">
    <div class="brand"><span class="brand__square"></span>Corvane Realty Partners</div>
    <p class="website">www.corvanerealty.example</p>
  </section>

  <section class="card card--back" aria-label="Card back">
    <div class="brand"><span class="brand__square"></span>Corvane Realty Partners</div>

    <address class="address">782 Marlowe Avenue San Francisco,<br>California 94127</address>

    <ul class="contacts">
      <li>
        <svg viewBox="0 0 14 12" aria-label="Office"><path d="M1 4c0-2 3-3 6-3s6 1 6 3v1h-3V4H4v1H1z"/><path d="M3 6h8l1 5H2z"/></svg>
        415-555-0142
      </li>
      <li>
        <svg viewBox="0 0 14 12" aria-label="Fax"><rect x="3" y="0" width="8" height="4"/><rect x="1" y="5" width="12" height="5"/><rect x="3" y="9" width="8" height="3"/></svg>
        415-555-0143
      </li>
      <li>
        <svg viewBox="0 0 14 12" aria-label="Cell"><rect x="1" y="8" width="2.5" height="4"/><rect x="4.5" y="5" width="2.5" height="7"/><rect x="8" y="2" width="2.5" height="10"/><rect x="11.5" y="0" width="2.5" height="12"/></svg>
        415-555-0186
      </li>
      <li>
        <svg viewBox="0 0 14 12" aria-label="Email"><path d="M1 2h12v9H1zM2 3v.5l5 4 5-4V3zm0 2v5h10V5L7 9z" fill-rule="evenodd"/></svg>
        ghanlon@corvanerealty.example
      </li>
    </ul>

    <div class="person">
      <p class="person__name">Gregory L. Hanlon</p>
      <p class="person__title">Marketing Manager</p>
    </div>

    <div class="accent"><span class="accent--navy"></span><span class="accent--green"></span></div>
  </section>
</main>
</body>
</html>
```